Business Card needed for International Migration and Education business

we are based in Australia, the business is called 'FarReach Relocation' and its sister business for international education is called 'FarReach Learning' - we need the design for the business 'FarReach Relocation' - FarReach Relocation is about migration to Australia (but not limited to Australia only therefore purely Australian look would not fit). We would like to see designs that use the color blue or acqua and maybe orange..all those colours don't have to be used together and not only those colours are to be used. We are looking for a modern design. The final design should communicate modern thinking, professionalism, dynamism, confidence. We would like to use the same business card design for our sister business "FarReach Learning" - which is business about studying in different countries as we recruit students to study in Australia, USA, New Zealand, Canada, UK etc. We would like to be able the final design to be easily changed by us to fit the 'FarReach Learning' business - we would only change the contact text (email address etc)

The information to be included in the business card: Tessa Virnaud Managing Director Migration Agent MARN 0917264 FarReach Relocation postal address: PO Box 2749, Carlwood East VIC 3179, Australia mobile: 0417296031 office address: Level 1, 287 Fenwick Road, Ardmere VIC 3211 web www.farreachrelocation-example.com telephone: 61 3 8714 6023 fax + 61 3 8735 2910 email: tessa@farreachrelocation-example.com

```html
<!DOCTYPE html>
<html lang="en">
<head>
<meta charset="utf-8">
<title>FarReach business cards</title>
<link rel="stylesheet" href="https://fonts.googleapis.com/css2?family=Arimo:wght@400;700&display=swap">
<style>
  :root {
    --stage: #000000;
    --band: #1b1a33;
    --card-dark: #1a1834;
    --card-light: #e4e4e4;
    --orange: #f26b21;
    --purple: #3d3566;
    --ink: #2b2b2b;
    --label: #3f3870;
    --heading: #9a9a9a;
    --globe-hi: #5a60b8;
    --globe-lo: #34357a;
    --peach: #edcfb8;
  }
  * { box-sizing: border-box; margin: 0; padding: 0; }
  html, body { width: 1200px; height: 1000px; overflow: hidden; background: var(--stage); }
  body { font-family: "Arimo", Arial, sans-serif; position: relative; }

  .section-title {
    position: absolute; left: 0; width: 1200px; text-align: center;
    color: var(--heading); font-size: 22px; letter-spacing: 3px; font-weight: 400;
  }
  .section-title.cards { top: 31px; }

  .card {
    position: absolute; width: 535px; height: 320px; border-radius: 22px; overflow: hidden;
  }
  .card.front { background: var(--card-dark); top: 90px; }
  .card.back { background: var(--card-light); top: 452px; }
  .card.left { left: 33px; }
  .card.right { left: 631px; }

  .artwork { position: absolute; }
  .front .artwork {
    right: 0; bottom: 0; width: 380px; height: 240px;
    background: radial-gradient(ellipse 100% 100% at 100% 100%, var(--globe-lo) 0%, var(--globe-hi) 55%, rgba(90,96,184,0) 100%);
  }
  .back .artwork {
    left: 0; bottom: 0; width: 360px; height: 235px;
    background: radial-gradient(ellipse 100% 100% at 0% 100%, var(--peach) 0%, var(--peach) 50%, rgba(237,207,184,0) 100%);
  }

  .brand-name {
    position: absolute; font-weight: 700; line-height: 1;
  }
  .front .brand-name { left: 20px; top: 32px; color: var(--orange); font-size: 50px; letter-spacing: -1px; }
  .front .brand-name span { display: block; font-size: 24px; letter-spacing: 0; margin-top: 6px; }
  .front.left .brand-name span { padding-left: 182px; }
  .front.right .brand-name span { padding-left: 196px; }
  .back .brand-name { right: 18px; top: 24px; color: var(--purple); font-size: 38px; text-align: right; letter-spacing: -1px; }
  .back .brand-name span { display: block; font-size: 19px; letter-spacing: 0; margin-top: 4px; }

  .person { position: absolute; left: 19px; top: 156px; }
  .person-name { font-size: 19px; font-weight: 700; color: var(--ink); }
  .person-role { font-size: 15px; color: var(--purple); margin-top: 1px; }

  .contacts { position: absolute; left: 19px; top: 213px; list-style: none; font-size: 13px; color: var(--ink); }
  .contacts li { display: flex; align-items: center; height: 17px; }
  .contacts li.gap { margin-top: 9px; }
  .contacts svg { width: 11px; height: 11px; margin-right: 6px; fill: var(--purple); }

  .addresses { position: absolute; left: 328px; top: 193px; font-size: 13px; color: var(--ink); line-height: 15px; }
  .right .addresses { left: 327px; top: 211px; }
  .addresses dt { font-size: 12.5px; font-weight: 700; color: var(--label); }
  .addresses dd + dt { margin-top: 4px; }
  .addresses .licence { margin-top: 6px; color: var(--label); font-size: 12.5px; }

  .logo-band { position: absolute; left: 0; top: 812px; width: 1200px; height: 188px; background: var(--band); }
  .section-title.logos { top: 18px; color: #8f8fa0; }
  .logo-sample {
    position: absolute; top: 62px; color: var(--orange); font-weight: 700; font-size: 66px;
    line-height: 1; letter-spacing: -2px; text-align: right; width: 366px;
  }
  .logo-sample span { display: block; font-size: 32px; letter-spacing: 0; margin-top: 4px; }
  .logo-sample.relocation { left: 118px; }
  .logo-sample.learning { left: 718px; }
</style>
</head>
<body>

<h2 class="section-title cards">+ MARTA AND NEIL CARDS</h2>

<section class="card front left">
  <div class="artwork" role="img" aria-label="Globe artwork area in soft blue tones"></div>
  <div class="brand-name">FarReach<span>Relocation</span></div>
</section>

<section class="card front right">
  <div class="artwork" role="img" aria-label="Globe artwork area in soft blue tones"></div>
  <div class="brand-name">FarReach<span>Learning</span></div>
</section>

<section class="card back left">
  <div class="artwork" role="img" aria-label="Faint globe artwork area in peach tones"></div>
  <div class="brand-name">FarReach<span>Relocation</span></div>

  <div class="person">
    <p class="person-name">Tessa Virnaud</p>
    <p class="person-role">Managing Director</p>
  </div>

  <ul class="contacts">
    <li><svg viewBox="0 0 12 12"><path d="M3 0h6v12H3zM4 1.5v7.5h4V1.5z"/></svg>041 729 6031</li>
    <li><svg viewBox="0 0 12 12"><path d="M0 4Q6 0 12 4v2H9V4H3v2H0zM2 7h8l1 5H1z"/></svg>(+61) 3 8714 6023</li>
    <li><svg viewBox="0 0 12 12"><path d="M3 0h6v4H3zM0 4h12v6H9v2H3v-2H0zM4 8v3h4V8z"/></svg>(+61) 3 8735 2910</li>
    <li class="gap"><svg viewBox="0 0 12 12"><path d="M0 2h12v8H0zM1 3l5 4 5-4z"/></svg>tessa@farreachrelocation-example.com</li>
    <li><svg viewBox="0 0 12 12"><circle cx="6" cy="6" r="6"/><path d="M6 1v10M1 6h10" stroke="#e4e4e4" stroke-width="1"/></svg>www.farreachrelocation-example.com</li>
  </ul>

  <dl class="addresses">
    <dt>Postal address:</dt>
    <dd>PO Box 2749, Carlwood East<br>VIC 3179, Australia</dd>
    <dt>Office address:</dt>
    <dd>Level 1, 287 Fenwick Road<br>Ardmere VIC 3211</dd>
    <dd class="licence">Migration Agent MARN 0917264</dd>
  </dl>
</section>

<section class="card back right">
  <div class="artwork" role="img" aria-label="Faint globe artwork area in peach tones"></div>
  <div class="brand-name">FarReach<span>Learning</span></div>

  <div class="person">
    <p class="person-name">Tessa Virnaud</p>
    <p class="person-role">Managing Director</p>
  </div>

  <ul class="contacts">
    <li><svg viewBox="0 0 12 12"><path d="M3 0h6v12H3zM4 1.5v7.5h4V1.5z"/></svg>041 729 6031</li>
    <li><svg viewBox="0 0 12 12"><path d="M0 4Q6 0 12 4v2H9V4H3v2H0zM2 7h8l1 5H1z"/></svg>(+61) 3 8714 6023</li>
    <li><svg viewBox="0 0 12 12"><path d="M3 0h6v4H3zM0 4h12v6H9v2H3v-2H0zM4 8v3h4V8z"/></svg>(+61) 3 8735 2910</li>
    <li class="gap"><svg viewBox="0 0 12 12"><path d="M0 2h12v8H0zM1 3l5 4 5-4z"/></svg>tessa@farreachlearning-example.com</li>
    <li><svg viewBox="0 0 12 12"><circle cx="6" cy="6" r="6"/><path d="M6 1v10M1 6h10" stroke="#e4e4e4" stroke-width="1"/></svg>www.farreachlearning-example.com</li>
  </ul>

  <dl class="addresses">
    <dt>Postal address:</dt>
    <dd>PO Box 2749, Carlwood East<br>VIC 3179, Australia</dd>
    <dt>Office address:</dt>
    <dd>Level 1, 287 Fenwick Road<br>Ardmere VIC 3211</dd>
  </dl>
</section>

<section class="logo-band">
  <h2 class="section-title logos">+ 8 LOGO FILE</h2>
  <div class="logo-sample relocation">FarReach<span>Relocation</span></div>
  <div class="logo-sample learning">FarReach<span>Learning</span></div>
</section>

</body>
</html>
```